galactic arcade 80s vibes - jewelry company

I am looking for someone to build me a website for my jewelry company - I am going for an 80s retro GALACTIC arcade vibe. I want it to feel old school, be brightly colored (purples, greens, etc) encompass planets, stars, or milky way type vibes. My company is called LumoKitt - it is zodiac signs & angel number jewelry. I want the website to open up as galaxy and my logo/name to pop up in the center of the screen and then go to the main page.

Industry/Entity Type

jewelry

Coding

Coded - Design and coding required

Number of Pages Required

1 page

Font styles to use
Other font styles liked:
• retro

Colors
0094D4
00A9DD
6FCCEA
C7EBF8
E9F6FB
00AB8E
00BBA5
67D7C9
C6EFE9
E9F9F6
59FF00
82FF00
B8FF75
E3FFCB
F4FFEA
FFF300
FFF600
FEFA6F
FFFEC7
FFFEE8
FFC000
F8CF3A
FAE287
FDF2CF
FEFAEE
E54698
E96AAD
F1A4CE
F9D9EA
FCEFF6
A7469A
B969AE
D3A5CF
EDDBEB
F8F0F9
6B429C
8869AF
B7A5CE
E3DAEB
F3F0F8

```html
<!DOCTYPE html>
<html lang="en">
<head>
<meta charset="utf-8">
<title>LumoKitt — Zodiac Signs &amp; Angel Number Jewelry</title>
<link href="https://fonts.googleapis.com/css2?family=Josefin+Sans:wght@300;400;600;700&display=swap" rel="stylesheet">
<style>
:root{
  --green:#59ff00;
  --green-deep:#4ce60a;
  --ink:#111111;
  --body:#555555;
  --muted:#8a8a8a;
  --white:#ffffff;
  --lilac:#e3daeb;
  --purple:#6b429c;
  --magenta:#a7469a;
  --pink:#e96aad;
  --night:#0d0b16;
}
*{margin:0;padding:0;box-sizing:border-box}
html,body{width:1200px;height:4397px;overflow:hidden}
body{position:relative;background:var(--white);font-family:"Josefin Sans",sans-serif;color:var(--ink)}
.abs{position:absolute}
.center{left:0;width:1200px;text-align:center}

/* header */
.site-header{top:0;left:0;width:1200px;height:99px;background:var(--white);z-index:3}
.brand-badge{left:85px;top:14px;width:150px;height:150px;border-radius:50%;background:radial-gradient(circle at 40% 35%,#4a3f9a,#1b1640 70%);border:6px solid var(--white);box-shadow:0 2px 8px rgba(0,0,0,.25);display:flex;align-items:center;justify-content:center;color:var(--green);font-weight:700;font-size:24px;z-index:4}
.main-nav a{position:absolute;top:42px;font-size:15px;color:var(--ink);text-decoration:none}
.main-nav a.active{color:var(--green-deep);font-weight:600}
.main-nav a.active::after{content:"";position:absolute;left:0;right:0;bottom:-7px;height:2px;background:var(--green-deep)}
.social-dot{width:17px;height:17px;border-radius:50%;background:var(--ink)}

/* hero */
.hero{top:99px;left:0;width:1200px;height:670px}
.hero-tagline{top:296px;font-size:18px;color:var(--white)}
.hero-title{top:344px;font-size:122px;font-weight:700;color:var(--green);letter-spacing:2px;line-height:1}
.btn-pill{display:flex;align-items:center;justify-content:center;border-radius:30px;font-size:16px;font-weight:600;text-decoration:none}
.hero-btn{left:502px;top:496px;width:192px;height:57px;background:var(--white);color:var(--ink);box-shadow:0 0 22px rgba(255,255,255,.75)}

/* section heads */
.eyebrow{font-size:20px;color:var(--green-deep)}
.heading{font-size:44px;font-weight:600;color:var(--ink)}
.lead{font-size:19px;line-height:29px;color:var(--muted)}

/* about */
.about-copy{left:85px;width:510px}
.about-text{font-size:21px;line-height:29px;color:var(--body)}
.btn-outline-green{left:85px;top:1242px;width:158px;height:60px;border:2px solid var(--green-deep);color:var(--green-deep)}
.about-shadow{left:692px;top:897px;width:440px;height:440px;background:var(--green)}
.about-photo{left:674px;top:881px;width:440px;height:440px;border-radius:6px;background:radial-gradient(circle at 30% 60%,#b8741a 0,transparent 22%),radial-gradient(circle at 75% 40%,#a7469a 0,transparent 25%),radial-gradient(circle at 45% 45%,#3a2a8a,#1a1550 60%,#0b0a25)}

/* zodiac */
.zodiac{top:1447px;left:0;width:1200px;height:584px;background:radial-gradient(ellipse at 50% 40%,#f0eef7,#dcd9ea 80%)}
.sign{width:176px;text-align:center}
.sign-mark{height:60px;display:flex;align-items:center;justify-content:center;font-size:46px;line-height:1;color:#1a1a1a}
.sign.selected .sign-mark{width:96px;height:96px;margin:-20px auto -16px;border-radius:50%;background:var(--green);color:var(--white)}
.sign-name{margin-top:14px;font-size:24px;color:var(--ink)}
.sign.selected .sign-name{color:var(--green-deep)}
.sign-desc{margin-top:8px;font-size:14px;line-height:20px;color:var(--muted)}

/* services */
.service-card{top:2333px;width:325px;height:414px;background:var(--white);border-radius:4px;box-shadow:0 2px 14px rgba(0,0,0,.08);text-align:center}
.service-card.featured{background:#000;color:var(--white)}
.service-icon{display:block;margin:36px auto 0}
.service-title{margin-top:22px;font-size:22px;font-weight:600}
.featured .service-title{color:var(--green)}
.service-text{margin:14px auto 0;width:250px;font-size:14px;line-height:19px;color:var(--body)}
.featured .service-text{color:var(--white)}
.btn-outline{margin:26px auto 0;width:160px;height:58px;border:2px solid #333;color:var(--ink)}
.featured .btn-outline{border-color:#444;color:var(--white)}

/* jewelry */
.jewelry-bg{top:2854px;left:0;width:1200px;height:740px;background:radial-gradient(ellipse at 88% 10%,rgba(180,120,100,.45),transparent 30%),linear-gradient(180deg,#4d6a73 0%,#7c8f99 30%,#c4c7cf 55%,#ffffff 80%)}
.jewelry-card{top:3156px;width:237px;height:413px;background:var(--white);border-radius:4px;box-shadow:0 2px 14px rgba(0,0,0,.08);text-align:center}
.jewel-photo{width:90px;height:196px;margin:36px auto 0;border-radius:45px;background:linear-gradient(180deg,#f3e2d6,#e6cdbc)}
.jewel-photo.silver{width:110px;background:linear-gradient(180deg,#eeeeee,#d4d4d4)}
.jewel-name{margin-top:26px;font-size:24px;font-weight:600}
.jewel-desc{margin:10px auto 0;width:140px;font-size:14px;line-height:20px;color:var(--muted)}
.add-cart{margin-top:18px;font-size:16px;font-weight:600}

/* contact */
.field{top:3742px;height:42px;border-bottom:1px solid #999;font-size:15px;padding:7px 12px}
.btn-notify{left:952px;top:3725px;width:161px;height:60px;border:2px solid #555;color:var(--ink)}

/* footer */
.site-footer{top:3892px;left:0;width:1200px;height:505px;background:radial-gradient(ellipse at 30% 20%,rgba(110,50,40,.55),transparent 45%),radial-gradient(ellipse at 70% 40%,rgba(90,40,50,.5),transparent 50%),linear-gradient(180deg,#1d1014,var(--night))}
.footer-badge{left:522px;top:3974px;width:154px;height:154px;border-radius:50%;background:radial-gradient(circle at 40% 35%,#4a3f9a,#1b1640 70%);border:4px solid var(--white);display:flex;align-items:center;justify-content:center;color:var(--green);font-weight:700;font-size:24px}
.footer-rule{left:85px;width:1028px;height:1px;background:rgba(255,255,255,.25)}
.footer-nav a{position:absolute;top:4222px;font-size:15px;color:var(--white);text-decoration:none}
.footer-small{color:var(--white)}
.footer-dot{width:16px;height:16px;border-radius:50%;background:var(--white)}
</style>
</head>
<body>

<header class="site-header abs">
  <nav class="main-nav">
    <a href="#" class="active" style="left:643px">Home</a>
    <a href="#" style="left:732px">About</a>
    <a href="#" style="left:820px">Services</a>
    <a href="#" style="left:922px">Contact</a>
  </nav>
  <span class="social-dot abs" style="left:1016px;top:41px" role="img" aria-label="Social link"></span>
  <span class="social-dot abs" style="left:1056px;top:41px" role="img" aria-label="Social link"></span>
  <span class="social-dot abs" style="left:1095px;top:41px" role="img" aria-label="Social link"></span>
</header>
<div class="brand-badge abs">LumoKitt</div>

<section class="hero abs">
  <svg width="1200" height="670" viewBox="0 0 1200 670" role="img" aria-label="Deep space galaxy with purple and magenta nebula over a glowing planet horizon">
    <defs>
      <linearGradient id="space" x1="0" y1="0" x2="0" y2="1">
        <stop offset="0" stop-color="#0a0818"/>
        <stop offset=".55" stop-color="#2a1150"/>
        <stop offset="1" stop-color="#5b2a8a"/>
      </linearGradient>
      <radialGradient id="magentaGlow" cx="62%" cy="58%" r="55%">
        <stop offset="0" stop-color="#f08ad0" stop-opacity=".95"/>
        <stop offset=".35" stop-color="#c44fb4" stop-opacity=".75"/>
        <stop offset=".7" stop-color="#6b2a9c" stop-opacity=".3"/>
        <stop offset="1" stop-color="#6b2a9c" stop-opacity="0"/>
      </radialGradient>
      <radialGradient id="haze" cx="18%" cy="35%" r="40%">
        <stop offset="0" stop-color="#8a7aa8" stop-opacity=".55"/>
        <stop offset="1" stop-color="#8a7aa8" stop-opacity="0"/>
      </radialGradient>
      <radialGradient id="haze2" cx="85%" cy="30%" r="30%">
        <stop offset="0" stop-color="#d36ac0" stop-opacity=".5"/>
        <stop offset="1" stop-color="#d36ac0" stop-opacity="0"/>
      </radialGradient>
      <radialGradient id="rim" cx="50%" cy="100%" r="50%">
        <stop offset="0" stop-color="#ffffff" stop-opacity=".9"/>
        <stop offset=".25" stop-color="#e6c8f5" stop-opacity=".6"/>
        <stop offset="1" stop-color="#b07ad8" stop-opacity="0"/>
      </radialGradient>
      <linearGradient id="planet" x1="0" y1="0" x2="0" y2="1">
        <stop offset="0" stop-color="#9a8fc4"/>
        <stop offset=".4" stop-color="#5a4f80"/>
        <stop offset="1" stop-color="#2a2540"/>
      </linearGradient>
      <clipPath id="heroClip"><path d="M0 0H1200V592Q600 720 0 592Z"/></clipPath>
    </defs>
    <g clip-path="url(#heroClip)">
      <rect width="1200" height="670" fill="url(#space)"/>
      <rect width="1200" height="670" fill="url(#haze)"/>
      <rect width="1200" height="670" fill="url(#haze2)"/>
      <rect width="1200" height="670" fill="url(#magentaGlow)"/>
      <ellipse cx="600" cy="540" rx="420" ry="120" fill="url(#rim)"/>
      <ellipse cx="600" cy="820" rx="560" ry="230" fill="url(#planet)"/>
    </g>
    <path d="M0 592Q600 720 1200 592V600Q600 745 0 618Z" fill="#59ff00"/>
  </svg>
</section>
<p class="hero-tagline abs center">LumoKitt is zodiac signs &amp; angel number jewelry.</p>
<h1 class="hero-title abs center">LUMOKITT</h1>
<a class="hero-btn btn-pill abs">Discover More</a>

<section class="about">
  <div class="about-copy abs" style="top:911px">
    <p class="eyebrow">About Us</p>
    <h2 class="heading" style="margin-top:12px">Welcome to LumoKitt</h2>
    <p class="about-text" style="margin-top:16px">Lorem ipsum dolor sit amet, consectetur adipiscing elit. Donec nec egestas tellus, et condimentum est. Aliquam interdum sapien porta mauris interdum, a hendrerit risus condimentum. Donec viverra augue ac tristique mattis. Nulla non purus mi. Aenean enim nisi, luctus eget mi id, finibus gravida ex.</p>
  </div>
  <a class="btn-outline-green btn-pill abs">Learn More</a>
  <div class="about-shadow abs"></div>
  <div class="about-photo abs" role="img" aria-label="Neon-lit retro arcade room with glowing cabinets"></div>
</section>

<section class="zodiac abs">
  <p class="eyebrow abs center" style="top:106px">Zodiac Sign</p>
  <h2 class="heading abs center" style="top:142px">Choose Your Zodiac Sign</h2>
  <p class="lead abs" style="left:225px;width:750px;top:206px;text-align:center">Lorem ipsum dolor sit amet, consectetur adipiscing elit. Donec nec egestas tellus, et condimentum est.</p>
  <div class="sign selected abs" style="left:74px;top:306px"><div class="sign-mark">&#9800;&#xFE0E;</div><p class="sign-name">Aries</p><p class="sign-desc">Lorem ipsum dolor<br>sit amet</p></div>
  <div class="sign abs" style="left:248px;top:306px"><div class="sign-mark">&#9801;&#xFE0E;</div><p class="sign-name">Taurus</p><p class="sign-desc">Lorem ipsum dolor<br>sit amet</p></div>
  <div class="sign abs" style="left:424px;top:306px"><div class="sign-mark">&#9802;&#xFE0E;</div><p class="sign-name">Gemini</p><p class="sign-desc">Lorem ipsum dolor<br>sit amet</p></div>
  <div class="sign abs" style="left:600px;top:306px"><div class="sign-mark">&#9803;&#xFE0E;</div><p class="sign-name">Cancer</p><p class="sign-desc">Lorem ipsum dolor<br>sit amet</p></div>
  <div class="sign abs" style="left:776px;top:306px"><div class="sign-mark">&#9804;&#xFE0E;</div><p class="sign-name">Leo</p><p class="sign-desc">Lorem ipsum dolor<br>sit amet</p></div>
  <div class="sign abs" style="left:952px;top:306px"><div class="sign-mark">&#9805;&#xFE0E;</div><p class="sign-name">Virgo</p><p class="sign-desc">Lorem ipsum dolor<br>sit amet</p></div>
</section>

<section class="services">
  <p class="eyebrow abs center" style="top:2135px">Our Services</p>
  <h2 class="heading abs center" style="top:2172px">Services We offer</h2>
  <p class="lead abs" style="left:260px;width:680px;top:2235px;text-align:center">Lorem ipsum dolor sit amet, consectetur adipiscing elit. Donec nec egestas tellus, et condimentum est.</p>
  <article class="service-card featured abs" style="left:85px">
    <svg class="service-icon" width="96" height="90" viewBox="0 0 96 90" role="img" aria-label="Planet with stars icon" fill="none" stroke="#fff" stroke-width="3">
      <circle cx="50" cy="48" r="20"/><ellipse cx="50" cy="48" rx="40" ry="11" transform="rotate(-18 50 48)"/>
      <path d="M14 6v16M6 14h16M84 4v12M78 10h12M12 66v14M5 73h14"/>
    </svg>
    <h3 class="service-title">Enter Service</h3>
    <p class="service-text">Curabitur cursus sapien pharetra pretium suscipit. Etiam eu neque rhoncus, eleifend ex ut, ornare leo. Cras ac orci orci. Proin mattis nisi consequat</p>
    <a class="btn-outline btn-pill">View More</a>
  </article>
  <article class="service-card abs" style="left:437px">
    <svg class="service-icon" width="96" height="90" viewBox="0 0 96 90" role="img" aria-label="Constellation icon" fill="none" stroke="#111" stroke-width="3">
      <path d="M10 24L30 50L62 36L70 14M30 50L40 64L66 58L62 36"/>
      <circle cx="10" cy="24" r="3"/><circle cx="30" cy="50" r="3"/><circle cx="62" cy="36" r="3"/><circle cx="70" cy="14" r="3"/><circle cx="40" cy="64" r="3"/><circle cx="66" cy="58" r="3"/>
      <path d="M86 2v14M79 9h14M24 74v14M17 81h14"/>
    </svg>
    <h3 class="service-title">Enter Service</h3>
    <p class="service-text">Curabitur cursus sapien pharetra pretium suscipit. Etiam eu neque rhoncus, eleifend ex ut, ornare leo. Cras ac orci orci. Proin mattis nisi consequat</p>
    <a class="btn-outline btn-pill">View More</a>
  </article>
  <article class="service-card abs" style="left:789px">
    <svg class="service-icon" width="96" height="90" viewBox="0 0 96 90" role="img" aria-label="Zodiac wheel icon" fill="none" stroke="#111" stroke-width="3">
      <circle cx="48" cy="45" r="40" stroke-dasharray="14 6"/><circle cx="48" cy="45" r="26"/><circle cx="48" cy="45" r="8"/>
      <path d="M48 19v10M48 61v10M22 45h10M64 45h10"/>
    </svg>
    <h3 class="service-title">Enter Service</h3>
    <p class="service-text">Curabitur cursus sapien pharetra pretium suscipit. Etiam eu neque rhoncus, eleifend ex ut, ornare leo. Cras ac orci orci. Proin mattis nisi consequat</p>
    <a class="btn-outline btn-pill">View More</a>
  </article>
</section>

<section class="jewelry">
  <div class="jewelry-bg abs" role="img" aria-label="Misty alien landscape with a ringed planet in the sky"></div>
  <p class="eyebrow abs center" style="top:2961px">Our Jewelry</p>
  <h2 class="heading abs center" style="top:2996px;color:var(--white)">Angel Number Jewelry</h2>
  <p class="lead abs" style="left:260px;width:680px;top:3060px;text-align:center;color:var(--white)">Lorem ipsum dolor sit amet, consectetur adipiscing elit. Donec nec egestas tellus, et condimentum est.</p>
  <article class="jewelry-card abs" style="left:85px"><div class="jewel-photo" role="img" aria-label="Rose gold angel pendant"></div><h3 class="jewel-name">Jewelry Name</h3><p class="jewel-desc">Lorem ipsum dolor sit amet</p><p class="add-cart">Add To Cart &nbsp;→</p></article>
  <article class="jewelry-card abs" style="left:348px"><div class="jewel-photo silver" role="img" aria-label="Silver angel pendant"></div><h3 class="jewel-name">Jewelry Name</h3><p class="jewel-desc">Lorem ipsum dolor sit amet</p><p class="add-cart">Add To Cart &nbsp;→</p></article>
  <article class="jewelry-card abs" style="left:613px"><div class="jewel-photo" role="img" aria-label="Rose gold angel pendant"></div><h3 class="jewel-name">Jewelry Name</h3><p class="jewel-desc">Lorem ipsum dolor sit amet</p><p class="add-cart">Add To Cart &nbsp;→</p></article>
  <article class="jewelry-card abs" style="left:876px"><div class="jewel-photo silver" role="img" aria-label="Silver angel pendant"></div><h3 class="jewel-name">Jewelry Name</h3><p class="jewel-desc">Lorem ipsum dolor sit amet</p><p class="add-cart">Add To Cart &nbsp;→</p></article>
</section>

<section class="contact">
  <h2 class="heading abs" style="left:85px;top:3670px">Get in Touch</h2>
  <div class="field abs" style="left:85px;width:376px">Name</div>
  <div class="field abs" style="left:509px;width:377px">Email</div>
  <a class="btn-notify btn-pill abs">Get Notified</a>
</section>

<footer class="site-footer abs" role="img" aria-label="Dark starry night sky"></footer>
<div class="footer-badge abs">LumoKitt</div>
<p class="footer-small abs center" style="top:4150px;font-size:18px">LumoKitt is zodiac signs &amp; angel number jewelry.</p>
<div class="footer-rule abs" style="top:4201px"></div>
<nav class="footer-nav">
  <a href="#" style="left:430px">Home</a>
  <a href="#" style="left:518px">About</a>
  <a href="#" style="left:606px">Services</a>
  <a href="#" style="left:708px">Contact</a>
</nav>
<div class="footer-rule abs" style="top:4254px"></div>
<p class="footer-small abs center" style="top:4283px;font-size:14px">© 2022. All Rights Reserved.</p>
<span class="footer-dot abs" style="left:550px;top:4328px" role="img" aria-label="Social link"></span>
<span class="footer-dot abs" style="left:591px;top:4328px" role="img" aria-label="Social link"></span>
<span class="footer-dot abs" style="left:629px;top:4328px" role="img" aria-label="Social link"></span>

</body>
</html>
```